Chewable Dog Supplements jar with lid

Below are some specifications of this project: 
There will be 6 different types of dog supplements in different jars, which will have different colors, or elements(dogs),  but will respect the same theme overall.  I attached some pictures below as a reference.
 The design I would like to create is for a label that will go around and on the top of a round plastic jar. The size of the product label is 25cm long and 8.5 cm high and on the top there is a circle that goes on the lid with the exact same design as on the front.
Some small pictures on the back with no Grain, Corn or Soy derivates  
 All products come in different shapes chews 
All products have 3 different headlines with their benefits that go on the front of the design.
All products have different flavors.
Regarding the text that will go on the back of the product, I can help with adding that to all products as long as we agree on how it looks. On the back I will need a space for a barcode, best before date, there should be 2 tables with ingredients and directions for use, and space for text under :Storage instructions, Warning, Description.

Target Market(s)

Europe

Industry/Entity Type

pet food

Requirements
Must have
• Trust signals ( Free from GMO, Natural ingredients, Free from artificial colouring) and a text box with the benefits of the product that I will provide.

```html
<!DOCTYPE html>
<html lang="en">
<head>
<meta charset="utf-8">
<title>Multivitamin Chews – Jar Label and Lid</title>
<link rel="stylesheet" href="https://fonts.googleapis.com/css2?family=Questrial&family=Baloo+2:wght@800&family=Oswald:wght@500&display=swap">
<style>
  :root {
    --cream: #fdefd0;
    --ink: #000000;
    --orange: #f5a344;
    --brown: #4a2a12;
    --white: #ffffff;
    --leaf: #7bbf2a;
    --photo-dark: #1e1d1c;
    --photo-mid: #4a4744;
    --photo-light: #d9d4cb;
  }
  html, body { margin: 0; padding: 0; overflow: hidden; background: var(--cream); }
  .canvas { display: block; width: 1200px; height: 1200px; }
  .body-text { font-family: "Questrial", sans-serif; }
  .title { font-family: "Baloo 2", sans-serif; font-weight: 800; }
  .count { font-family: "Oswald", sans-serif; font-weight: 500; }
  .brand { font-family: "Questrial", sans-serif; letter-spacing: 2px; }
</style>
</head>
<body>
<svg class="canvas" viewBox="0 0 1200 1200" xmlns="http://www.w3.org/2000/svg">
  <defs>
    <linearGradient id="photo-tone" x1="0" y1="0" x2="0.3" y2="1">
      <stop offset="0" stop-color="var(--photo-dark)"/>
      <stop offset="0.6" stop-color="var(--photo-mid)"/>
      <stop offset="1" stop-color="var(--photo-light)"/>
    </linearGradient>
    <symbol id="paw" viewBox="0 0 20 20">
      <ellipse cx="10" cy="14" rx="5" ry="4.2"/>
      <ellipse cx="4" cy="8.5" rx="2.2" ry="2.8"/>
      <ellipse cx="8" cy="4.5" rx="2.2" ry="2.8"/>
      <ellipse cx="13" cy="4.5" rx="2.2" ry="2.8"/>
      <ellipse cx="17" cy="8.5" rx="2.2" ry="2.8"/>
    </symbol>
    <clipPath id="lid-clip"><circle cx="620" cy="874" r="273"/></clipPath>
  </defs>

  <!-- Wrap label -->
  <g class="wrap-label">
    <rect class="band-top" x="0" y="43" width="1200" height="134" fill="var(--ink)"/>
    <rect class="band-main" x="0" y="177" width="1200" height="376" fill="var(--orange)"/>

    <g class="about-panel body-text">
      <rect x="-20" y="91" width="270" height="443" rx="18" fill="none" stroke="var(--white)" stroke-width="2.5"/>
      <text x="0" y="129" font-size="28" fill="var(--white)">DESPRE PRODUS</text>
      <text x="3" y="165" font-size="16.5" fill="var(--white)">Soft Chew (2.5g):</text>
      <g font-size="16" fill="var(--ink)">
        <text x="-3" y="202">p</text>
        <text x="-3" y="237">hanvre</text>
        <text x="-3" y="362">gembre</text>
        <g text-anchor="end">
          <text x="124" y="202">200mg</text>
          <text x="124" y="238">200mg</text>
          <text x="124" y="274">200mg</text>
          <text x="124" y="292">200mg</text>
          <text x="124" y="310">120mg</text>
          <text x="124" y="328">90mg</text>
          <text x="124" y="346">80mg</text>
          <text x="124" y="364">80mg</text>
          <text x="124" y="400">50mg</text>
          <text x="124" y="418">25mg</text>
        </g>
      </g>
      <g font-size="16.5" fill="var(--ink)">
        <text x="-3" y="449">rem ipsum dolor sit amet,</text>
        <text x="-3" y="467">elit, sed diam nonummy</text>
        <text x="-3" y="485">ut laoreet dolore magna</text>
        <text x="-3" y="503">Ut wisi enim ad minim</text>
        <text x="-3" y="521">erci tation ullamcorper</text>
      </g>
    </g>

    <rect class="hero-photo" role="img" aria-label="Photo of a black and white dog looking up to the right"
      x="266" y="140" width="346" height="413" fill="url(#photo-tone)"/>

    <g class="brand-mark">
      <rect x="376" y="99" width="80" height="69" fill="var(--ink)"/>
      <text class="brand" x="416" y="163" font-size="10" fill="var(--white)" text-anchor="middle">PAWVITA</text>
    </g>

    <g class="pack-count" fill="var(--white)">
      <text class="count" x="375" y="465" font-size="46">60</text>
      <text class="count" font-size="17" transform="translate(425 420) rotate(90)">CHEWS</text>
      <text class="body-text" x="369" y="497" font-size="13" font-weight="700">NET</text>
      <text class="body-text" x="406" y="497" font-size="12">5.29 oz</text>
      <text class="body-text" x="376" y="515" font-size="13" font-weight="700">WT</text>
      <text class="body-text" x="406" y="515" font-size="12">(150g)</text>
    </g>

    <text class="title" x="600" y="158" font-size="84" fill="var(--white)" textLength="380" lengthAdjust="spacingAndGlyphs">Multivitamin</text>
    <text class="title" x="694" y="241" font-size="68" fill="var(--brown)" textLength="197" lengthAdjust="spacingAndGlyphs">CHEWS</text>
    <text class="body-text" x="674" y="299" font-size="28" fill="var(--ink)" textLength="235" lengthAdjust="spacingAndGlyphs">SALMON FLAVOR</text>

    <g class="benefits body-text" font-size="16.5" fill="var(--ink)">
      <use href="#paw" x="705" y="346" width="20" height="20"/>
      <text x="736" y="363">Strong Immunity</text>
      <line x1="735" y1="376" x2="907" y2="376" stroke="var(--ink)" stroke-width="1"/>
      <use href="#paw" x="705" y="380" width="20" height="20"/>
      <text x="736" y="397">Hip and Joint Support</text>
      <line x1="735" y1="410" x2="907" y2="410" stroke="var(--ink)" stroke-width="1"/>
      <use href="#paw" x="705" y="414" width="20" height="20"/>
      <text x="736" y="431">Skin and Coat Health</text>
    </g>

    <g class="trust-badges">
      <circle cx="737" cy="495" r="25" fill="none" stroke="var(--ink)" stroke-width="2"/>
      <rect x="786" y="476" width="37" height="37" rx="10" fill="var(--leaf)"/>
      <text class="body-text" x="827" y="492" font-size="10.5" fill="var(--ink)" font-weight="700">SUPPORT</text>
      <text class="body-text" x="827" y="505" font-size="10.5" fill="var(--ink)" font-weight="700">FOR DOGS</text>
    </g>

    <g class="info-column body-text" fill="var(--ink)">
      <text x="1068" y="218" font-size="21">CAUTIONS (F</text>
      <g font-size="15">
        <text x="1068" y="236">Lorem ipsum dolo</text>
        <text x="1068" y="254">adipiscing elit, sed</text>
        <text x="1068" y="272">.euismod tincidunt</text>
        <text x="1068" y="290">aliquam erat volut</text>
        <text x="1068" y="308">Ut wisi enim ad m</text>
        <text x="1068" y="326">exerci tation ullam</text>
      </g>
      <text x="1068" y="368" font-size="21">WARNINGS(A</text>
      <g font-size="15">
        <text x="1068" y="387">Suscipit lobortis n</text>
        <text x="1068" y="405">commodo conseq</text>
        <text x="1068" y="423">iriure dolor in hen</text>
      </g>
      <g font-size="15">
        <text x="1068" y="458">IMPORTATOR:</text>
        <text x="1068" y="476">Northvale Trade Ltd</text>
        <text x="1068" y="494">Iasi, Strada Florilor</text>
        <text x="1068" y="512">info@pawvita.ro</text>
        <text x="1068" y="530">pawvita.ro</text>
      </g>
    </g>
  </g>

  <!-- Lid label -->
  <g class="lid-label" clip-path="url(#lid-clip)">
    <rect x="340" y="590" width="560" height="206" fill="var(--ink)"/>
    <rect x="340" y="796" width="560" height="360" fill="var(--orange)"/>

    <rect class="hero-photo" role="img" aria-label="Photo of a black and white dog looking up to the right"
      x="358" y="730" width="258" height="420" fill="url(#photo-tone)"/>

    <g class="brand-mark">
      <rect x="447" y="711" width="62" height="56" fill="var(--ink)"/>
      <text class="brand" x="478" y="763" font-size="8" fill="var(--white)" text-anchor="middle">PAWVITA</text>
    </g>

    <g class="pack-count" fill="var(--brown)">
      <text class="count" x="463" y="1022" font-size="36">60</text>
      <text class="count" font-size="13" transform="translate(507 989) rotate(90)">CHEWS</text>
    </g>
    <g class="body-text" fill="var(--ink)">
      <text x="458" y="1051" font-size="11" font-weight="700">NET</text>
      <text x="489" y="1051" font-size="9">5.29 oz</text>
      <text x="464" y="1066" font-size="11" font-weight="700">WT</text>
      <text x="489" y="1066" font-size="9">(150g)</text>
    </g>

    <text class="title" x="589" y="780" font-size="58" fill="var(--white)" textLength="258" lengthAdjust="spacingAndGlyphs">Multivitamin</text>
    <text class="title" x="652" y="838" font-size="46" fill="var(--brown)" textLength="134" lengthAdjust="spacingAndGlyphs">CHEWS</text>
    <text class="body-text" x="638" y="893" font-size="20" fill="var(--ink)" textLength="177" lengthAdjust="spacingAndGlyphs">SALMON FLAVOR</text>

    <g class="benefits body-text" font-size="14" fill="var(--ink)">
      <use href="#paw" x="593" y="983" width="17" height="17"/>
      <text x="621" y="998">Strong Immunity</text>
      <line x1="619" y1="1009" x2="770" y2="1009" stroke="var(--ink)" stroke-width="1"/>
      <use href="#paw" x="593" y="1012" width="17" height="17"/>
      <text x="621" y="1027">Hip and Joint Support</text>
      <line x1="619" y1="1038" x2="770" y2="1038" stroke="var(--ink)" stroke-width="1"/>
      <use href="#paw" x="593" y="1041" width="17" height="17"/>
      <text x="621" y="1056">Skin and Coat Health</text>
    </g>

    <g class="trust-badges">
      <circle cx="613" cy="1095" r="18" fill="none" stroke="var(--ink)" stroke-width="1.6"/>
      <rect x="650" y="1080" width="27" height="27" rx="7" fill="var(--leaf)"/>
      <text class="body-text" x="681" y="1093" font-size="8" fill="var(--ink)" font-weight="700">SUPPORT</text>
      <text class="body-text" x="681" y="1102" font-size="8" fill="var(--ink)" font-weight="700">FOR DOGS</text>
    </g>
  </g>
</svg>
</body>
</html>
```